Stationary for Halcyon Elite Las Vegas
Business cards & letter head, etc
Stationary for Halcyon Elite Las Vegas - Hospitality Industry
Creative Brief
Use same font as used in my logo
Just make it look nice & professional
Professional
Miles Grant
Co-Founder and Managing Partner
We don't want an address listed
miles.t.grant@mailbox-demo.net
www.halcyonelitelasvegas-demo.com
We also need a second card with all of the same info except for the following changes: Name: Derek Malone Phone #: 555.014.7392 Email: Derek.Malonevip@mailbox-demo.net
Just use the logo

```html
<!DOCTYPE html>
<html lang="en">
<head>
<meta charset="utf-8">
<title>Halcyon Elite Las Vegas — Business Card</title>
<link href="https://fonts.googleapis.com/css2?family=Quicksand:wght@400;500;600&display=swap" rel="stylesheet">
<style>
  :root {
    --page-bg: #e9ecef;
    --card-white: #ffffff;
    --brand-blue: #1f6fd0;
    --brand-blue-deep: #1a5fbf;
    --brand-blue-light: #3fb0ef;
    --ink-white: #ffffff;
    --ink-soft: rgba(255,255,255,0.85);
  }
  * { box-sizing: border-box; margin: 0; padding: 0; }
  html, body {
    width: 1200px; height: 1009px; overflow: hidden;
    background: var(--page-bg);
    font-family: "Quicksand", sans-serif;
  }
  .sheet {
    position: relative; width: 1200px; height: 1009px;
  }
  .card {
    position: absolute; left: 220px; width: 760px; height: 434px;
    border-radius: 34px; overflow: hidden;
    box-shadow: 0 6px 22px rgba(0,0,0,0.12);
  }
  .card--front { top: 47px; background: var(--card-white); }
  .card--back {
    top: 528px;
    background: linear-gradient(160deg, var(--brand-blue-deep) 0%, var(--brand-blue) 45%, var(--brand-blue-light) 100%);
  }

  /* front */
  .brand {
    position: absolute; left: 44px; top: 118px; width: 300px;
    color: var(--brand-blue); font-weight: 500;
  }
  .brand__name { font-size: 46px; line-height: 1; letter-spacing: -1px; text-transform: lowercase; }
  .brand__city { font-size: 24px; letter-spacing: 9px; text-transform: uppercase; margin-top: 8px; }
  .brand__tag { font-size: 11px; letter-spacing: 1px; margin-top: 6px; text-transform: lowercase; }

  .contact-panel {
    position: absolute; left: 354px; top: 34px; right: 0; bottom: 0;
    border-top-left-radius: 34px;
    background: linear-gradient(165deg, var(--brand-blue-deep) 0%, var(--brand-blue) 50%, var(--brand-blue-light) 100%);
    color: var(--ink-white);
    padding: 58px 0 0 40px;
  }
  .contact__name { font-size: 22px; font-weight: 500; }
  .contact__title { font-size: 14px; color: var(--ink-soft); margin-top: 4px; }
  .contact__list { list-style: none; margin-top: 58px; }
  .contact__item {
    display: flex; align-items: center; gap: 10px;
    font-size: 14px; line-height: 1; margin-bottom: 12px;
  }
  .contact__icon { width: 14px; height: 14px; flex: none; }

  /* back */
  .back-brand {
    position: absolute; right: 70px; bottom: 100px;
    color: var(--ink-white); font-weight: 500; text-align: right;
  }
  .back-brand__name { font-size: 60px; line-height: 1; letter-spacing: -1px; text-transform: lowercase; }
  .back-brand__url { font-size: 15px; letter-spacing: 3px; margin-top: 10px; }
</style>
</head>
<body>
<main class="sheet">
  <section class="card card--front" aria-label="Business card front">
    <div class="brand">
      <div class="brand__name">halcyon elite</div>
      <div class="brand__city">Las Vegas</div>
      <div class="brand__tag">vip hosting &amp; nightlife concierge</div>
    </div>

    <div class="contact-panel">
      <div class="contact__name">Miles Grant</div>
      <div class="contact__title">Co-Founder and Managing Partner</div>
      <ul class="contact__list">
        <li class="contact__item">
          <svg class="contact__icon" viewBox="0 0 14 14" aria-hidden="true"><path d="M3 1.5 L5.2 1.5 L6 4.5 L4.6 5.6 C5.3 7.2 6.6 8.6 8.3 9.4 L9.4 8 L12.5 8.8 L12.5 11 C12.5 11.9 11.8 12.5 11 12.5 C5.8 12.2 1.8 8.2 1.5 3 C1.5 2.2 2.1 1.5 3 1.5 Z" fill="#fff"/></svg>
          <span>555.014.7392</span>
        </li>
        <li class="contact__item">
          <svg class="contact__icon" viewBox="0 0 14 14" aria-hidden="true"><rect x="1" y="3" width="12" height="8.5" rx="1.2" fill="none" stroke="#fff" stroke-width="1.3"/><path d="M1.5 3.6 L7 8 L12.5 3.6" fill="none" stroke="#fff" stroke-width="1.3"/></svg>
          <span>miles.t.grant@mailbox-demo.net</span>
        </li>
        <li class="contact__item">
          <svg class="contact__icon" viewBox="0 0 14 14" aria-hidden="true"><circle cx="7" cy="7" r="5.6" fill="none" stroke="#fff" stroke-width="1.2"/><ellipse cx="7" cy="7" rx="2.4" ry="5.6" fill="none" stroke="#fff" stroke-width="1.1"/><path d="M1.4 7 H12.6" stroke="#fff" stroke-width="1.1"/></svg>
          <span>www.halcyonelitelasvegas-demo.com</span>
        </li>
      </ul>
    </div>
  </section>

  <section class="card card--back" aria-label="Business card back">
    <div class="back-brand">
      <div class="back-brand__name">halcyon elite</div>
      <div class="back-brand__url">www.halcyonelitelasvegas-demo.com</div>
    </div>
  </section>
</main>
</body>
</html>
```